Lotus Leaf Kitchen Road Billboard

Road Billboard I need all of this information on it
Authentic Thai Food Bangkok Style
6.5 Miles on the right
4126 Maple Ridge Rd Otto NC
828-555-4172

```html
<!DOCTYPE html>
<html lang="en">
<head>
<meta charset="utf-8">
<title>Lotus Leaf Kitchen – Road Billboard</title>
<link rel="stylesheet" href="https://fonts.googleapis.com/css2?family=Oswald:wght@500;700&display=swap">
<style>
  :root {
    --page-bg: #e86c00;
    --board-yellow: #f8cf35;
    --smoke-dark: #1d1f1f;
    --wok-black: #151515;
    --flame-deep: #c4501a;
    --flame-orange: #ee8a24;
    --flame-gold: #f9c14a;
    --greens: #4f6b2a;
    --type-red: #a8161c;
    --type-white: #ffffff;
  }
  * { margin: 0; padding: 0; box-sizing: border-box; }
  html, body {
    width: 925px;
    height: 1200px;
    overflow: hidden;
    background: var(--page-bg);
  }
  .billboard {
    position: absolute;
    left: 40px;
    top: 389px;
    width: 845px;
    height: 422px;
    background: var(--board-yellow);
    overflow: hidden;
    box-shadow: 0 6px 18px rgba(0, 0, 0, 0.35);
    font-family: "Oswald", "Arial Narrow", sans-serif;
  }
  .billboard__art {
    position: absolute;
    inset: 0;
    width: 100%;
    height: 100%;
  }
  .outlined {
    position: absolute;
    color: var(--type-white);
    white-space: nowrap;
    line-height: 1;
    transform-origin: left top;
    text-shadow:
      -2px -2px 0 var(--type-red), 2px -2px 0 var(--type-red),
      -2px 2px 0 var(--type-red), 2px 2px 0 var(--type-red),
      0 -2px 0 var(--type-red), 0 2px 0 var(--type-red),
      -2px 0 0 var(--type-red), 2px 0 0 var(--type-red),
      0 0 3px var(--type-red);
  }
  .headline {
    left: 51px;
    top: 58px;
    font-size: 47px;
    font-weight: 700;
    letter-spacing: -0.5px;
    transform: scaleX(0.9);
  }
  .directions__arrow {
    position: absolute;
    left: 55px;
    top: 126px;
    width: 78px;
    height: 22px;
  }
  .directions__just {
    left: 144px;
    top: 107px;
    font-size: 50px;
    font-weight: 700;
    color: var(--board-yellow);
    transform: scaleX(0.88);
  }
  .directions__distance {
    left: 230px;
    top: 111px;
    font-size: 42px;
    font-weight: 500;
    transform: scaleX(0.8);
  }
  .brand {
    position: absolute;
    left: 50px;
    top: 182px;
    width: 180px;
    display: flex;
    flex-direction: column;
    align-items: center;
    gap: 12px;
  }
  .brand__mark {
    width: 86px;
    height: 86px;
    border-radius: 50%;
    background: var(--type-white);
  }
  .brand__name {
    color: var(--type-white);
    font-weight: 500;
    font-size: 24px;
    line-height: 1;
    white-space: nowrap;
  }
  .address {
    left: 47px;
    top: 340px;
    font-size: 38px;
    font-weight: 500;
    transform: scaleX(0.7);
  }
  .phone {
    left: 627px;
    top: 340px;
    font-size: 38px;
    font-weight: 500;
    transform: scaleX(0.72);
  }
</style>
</head>
<body>
  <section class="billboard">
    <svg class="billboard__art" viewBox="0 0 845 422" preserveAspectRatio="none">
      <defs>
        <radialGradient id="flameUpper" cx="0.85" cy="0.3" r="0.35">
          <stop offset="0" stop-color="var(--flame-gold)"/>
          <stop offset="0.45" stop-color="var(--flame-orange)" stop-opacity="0.85"/>
          <stop offset="1" stop-color="var(--flame-deep)" stop-opacity="0"/>
        </radialGradient>
        <radialGradient id="flameLower" cx="0.5" cy="0.88" r="0.28">
          <stop offset="0" stop-color="var(--flame-gold)"/>
          <stop offset="0.5" stop-color="var(--flame-orange)" stop-opacity="0.8"/>
          <stop offset="1" stop-color="var(--flame-deep)" stop-opacity="0"/>
        </radialGradient>
        <radialGradient id="foodGlow" cx="0.55" cy="0.4" r="0.22">
          <stop offset="0" stop-color="var(--greens)"/>
          <stop offset="0.6" stop-color="#6a4a2a" stop-opacity="0.6"/>
          <stop offset="1" stop-color="var(--smoke-dark)" stop-opacity="0"/>
        </radialGradient>
      </defs>
      <g role="img" aria-label="Photograph of a flaming wok with tossed shrimp and vegetables">
        <polygon fill="var(--smoke-dark)"
          points="393,0 845,0 845,422 139,422 170,395 200,365 225,330 232,300 240,270 258,245 273,200 285,170 300,140 330,110 350,70 372,35"/>
        <rect x="0" y="0" width="845" height="422" fill="url(#foodGlow)"/>
        <rect x="0" y="0" width="845" height="422" fill="url(#flameUpper)"/>
        <rect x="0" y="0" width="845" height="422" fill="url(#flameLower)"/>
      </g>
      <g fill="var(--board-yellow)">
        <polygon points="845,30 845,46 700,140 692,134"/>
        <polygon points="845,245 845,262 660,380 652,373"/>
        <polygon points="845,330 845,422 760,422"/>
        <polygon points="590,0 640,0 560,40"/>
      </g>
    </svg>

    <h1 class="headline outlined">Authentic Thai Food Bangkok Style</h1>

    <svg class="directions__arrow" viewBox="0 0 78 22" aria-hidden="true">
      <path d="M2 9 L64 12" stroke="var(--type-red)" stroke-width="3" fill="none"/>
      <path d="M54 2 L77 12 L54 21 L61 12 Z" fill="var(--type-red)"/>
    </svg>
    <span class="directions__just outlined">Just</span>
    <span class="directions__distance outlined">6.5 MILES ON THE RIGHT</span>

    <div class="brand">
      <span class="brand__mark"></span>
      <span class="brand__name">Lotus Leaf Kitchen</span>
    </div>

    <p class="address outlined">4126 MAPLE RIDGE RD OTTO NC</p>
    <p class="phone outlined">828-555-4172</p>
  </section>
</body>
</html>
```